Veldon Tracing, Inc. - Stationary Project
Business Cards and Stationary for Missing Person Consultants
Professional
Luke Hammond
Search Coordinator
718 West Marlow Avenue
Suite #263
Orlando, FL 32806
lhammond@veldontracing-demo.org
www.VeldonTracing-demo.org
Our organization is called upon
when someone disappears. We¹d like to have a professional business card that
is very eye-catching and people will notice. Please use the red, black and
gray colors in the logo to make a great looking business card, letterhead
and envelope. We look forward to seeing your designs.
We'd like to see a clever use of the logo on the back of the card in bigger format.
This is our logo in AI format.

```html
<!DOCTYPE html>
<html lang="en">
<head>
<meta charset="utf-8">
<title>Veldon Tracing, Inc. – Business Cards</title>
<link rel="stylesheet" href="https://fonts.googleapis.com/css2?family=Arimo:wght@400;700&display=swap">
<style>
  :root {
    --stage: #5a5a5c;
    --red: #c8101e;
    --red-dark: #8e0a14;
    --ink: #1c1c1c;
    --card-light: #ffffff;
    --card-dark: #262626;
    --card-dark-2: #3a3a3a;
    --grey: #8a8a8a;
    --white: #ffffff;
  }
  * { margin: 0; padding: 0; box-sizing: border-box; }
  html, body { width: 1200px; height: 768px; overflow: hidden; }
  body {
    background: var(--stage);
    font-family: "Arimo", Arial, sans-serif;
    position: relative;
  }
  .card {
    position: absolute;
    width: 468px;
    height: 266px;
    overflow: hidden;
    box-shadow: 0 4px 10px rgba(0,0,0,.35);
  }
  .card--light { background: var(--card-light); color: var(--ink); }
  .card--dark { background: linear-gradient(160deg, var(--card-dark-2), var(--card-dark)); color: var(--white); }
  .front-left { left: 120px; top: 187px; }
  .front-right { left: 612px; top: 187px; }
  .back-left { left: 120px; top: 473px; }
  .back-right { left: 612px; top: 473px; }

  .card__swoosh { position: absolute; inset: 0; width: 100%; height: 100%; }

  .holder { position: absolute; right: 20px; top: 12px; text-align: right; color: var(--white); }
  .holder__name { font-size: 21px; font-weight: 700; line-height: 1.1; }
  .holder__title { font-size: 12px; font-weight: 400; margin-top: 2px; }

  .brand { position: absolute; display: flex; align-items: center; gap: 12px; }
  .brand__dot { border-radius: 50%; background: var(--red); flex: none; }
  .brand__name { font-weight: 700; white-space: nowrap; letter-spacing: -0.5px; }
  .card--light .brand__name { color: var(--ink); }
  .card--dark .brand__name { color: var(--white); }

  .front .brand { left: 26px; top: 112px; }
  .front .brand__dot { width: 46px; height: 46px; }
  .front .brand__name { font-size: 30px; }

  .address {
    position: absolute; right: 22px; top: 155px;
    font-size: 9px; line-height: 1.35; text-align: right;
  }
  .contact-line {
    position: absolute; right: 22px; bottom: 14px;
    font-size: 8.5px; text-align: right; white-space: nowrap;
  }

  .back .brand { left: 50%; top: 92px; transform: translateX(-50%); }
  .back .brand__dot { width: 64px; height: 64px; }
  .back .brand__name { font-size: 40px; }
  .back__web {
    position: absolute; left: 0; right: 0; bottom: 16px;
    text-align: center; font-size: 11px;
  }
</style>
</head>
<body>

<section class="card card--light front front-left">
  <svg class="card__swoosh" viewBox="0 0 468 266" aria-hidden="true">
    <path d="M0,0 H468 V70 C360,58 250,68 120,104 C70,118 30,128 0,132 Z" fill="var(--red)"/>
    <path d="M0,132 C30,128 70,118 120,104 C250,68 360,58 468,70 V76 C360,66 250,76 124,110 C74,123 32,133 0,138 Z" fill="var(--ink)"/>
    <path d="M0,0 H468 V70 C360,58 250,68 120,104 C70,118 30,128 0,132 Z" fill="var(--white)" opacity="0" />
    <path d="M0,0 H210 C150,30 80,50 0,62 Z" fill="var(--white)"/>
  </svg>
  <div class="holder">
    <p class="holder__name">Luke Hammond</p>
    <p class="holder__title">Search Coordinator</p>
  </div>
  <div class="brand">
    <span class="brand__dot"></span>
    <span class="brand__name">Veldon Tracing</span>
  </div>
  <p class="address">718 West Marlow Avenue<br>Suite #263<br>Orlando, FL 32806<br><br>Cell: (407) 555-0148 &nbsp;|&nbsp; Fax: (407) 555-0192</p>
  <p class="contact-line">Email: lhammond@veldontracing-demo.org &nbsp;|&nbsp; Web: www.VeldonTracing-demo.org</p>
</section>

<section class="card card--dark front front-right">
  <svg class="card__swoosh" viewBox="0 0 468 266" aria-hidden="true">
    <path d="M0,0 H468 V70 C360,58 250,68 120,104 C70,118 30,128 0,132 Z" fill="var(--red)"/>
    <path d="M0,132 C30,128 70,118 120,104 C250,68 360,58 468,70 V76 C360,66 250,76 124,110 C74,123 32,133 0,138 Z" fill="var(--grey)"/>
    <path d="M0,0 H210 C150,30 80,50 0,62 Z" fill="var(--card-dark-2)"/>
  </svg>
  <div class="holder">
    <p class="holder__name">Luke Hammond</p>
    <p class="holder__title">Search Coordinator</p>
  </div>
  <div class="brand">
    <span class="brand__dot"></span>
    <span class="brand__name">Veldon Tracing</span>
  </div>
  <p class="address">718 West Marlow Avenue<br>Suite #263<br>Orlando, FL 32806<br><br>Cell: (407) 555-0148 &nbsp;|&nbsp; Fax: (407) 555-0192</p>
  <p class="contact-line">Email: lhammond@veldontracing-demo.org &nbsp;|&nbsp; Web: www.VeldonTracing-demo.org</p>
</section>

<section class="card card--light back back-left">
  <div class="brand">
    <span class="brand__dot"></span>
    <span class="brand__name">Veldon Tracing</span>
  </div>
  <p class="back__web">www.VeldonTracing-demo.org</p>
</section>

<section class="card card--dark back back-right">
  <div class="brand">
    <span class="brand__dot"></span>
    <span class="brand__name">Veldon Tracing</span>
  </div>
  <p class="back__web">www.VeldonTracing-demo.org</p>
</section>

</body>
</html>
```